Enter the secret world of social tradecraft

Design a stunning work of art that markets our product "Quillmark: A Hidden Ledger of Social Outreach Craftwork"

We need a set of assets for using in building our wordpress site and marketing materials. We'd like to have those assets delivered as a ONE PAGE HTML5 LANDING PAGE example.

We have a video that gives the look and feel of that we are going for and would like to extend it into a landing page for now with a customized logo to be included.

Watch the video here: https://www.vidstreamhub.example/watch?v=Qm7RtLp2Wz9

The product is an informational product containing information on TZ marketing.

The final design should be intriguing and draw in the user with hints of intrigue.

Target Market(s)

Online Marketers

Industry/Entity Type

Marketing

Requirements
Must have
• Must match video in look and feel; must be html5 and responsive
Nice to have
• inventive html animations or css transitions

```html
<!DOCTYPE html>
<html lang="en">
<head>
<meta charset="utf-8">
<title>Quillmark: A Hidden Ledger of Social Outreach Craftwork</title>
<link rel="stylesheet" href="https://fonts.googleapis.com/css2?family=Cinzel:wght@400;700&display=swap">
<style>
  :root {
    --ink: #000000;
    --bar: #060606;
    --bar-line: #1e1e1e;
    --smoke-1: #2a2a2a;
    --smoke-2: #0b0b0b;
    --chalk: #f4f4f4;
    --logo-chalk: #d9d9d9;
    --frame: #3b3b3b;
    --screen-1: #1c1a1d;
    --screen-2: #070607;
    --button-bg: #f1f3f4;
    --button-ink: #0c0c0c;
    --accent-red: #c9221c;
  }
  * { box-sizing: border-box; margin: 0; padding: 0; }
  html, body { width: 1200px; height: 875px; overflow: hidden; background: var(--ink); }
  .page {
    position: relative;
    width: 1200px;
    height: 875px;
    overflow: hidden;
    background:
      radial-gradient(ellipse 420px 300px at 600px 250px, var(--smoke-1) 0%, transparent 75%),
      radial-gradient(ellipse 300px 240px at 1080px 150px, #1d1d1d 0%, transparent 70%),
      radial-gradient(ellipse 380px 260px at 140px 480px, #161616 0%, transparent 70%),
      linear-gradient(180deg, var(--smoke-2) 0%, #141414 40%, var(--ink) 100%);
    font-family: 'Cinzel', 'Trajan Pro', serif;
    color: var(--chalk);
  }
  .topbar {
    position: absolute; left: 0; top: 0;
    width: 1200px; height: 55px;
    background: var(--bar);
    border-bottom: 1px solid var(--bar-line);
  }
  .menu-toggle {
    position: absolute; left: 0; top: 0;
    width: 59px; height: 55px;
    background: #1a1a1a;
    border-right: 1px solid var(--bar-line);
  }
  .menu-toggle span {
    position: absolute; left: 15px;
    width: 30px; height: 4px;
    background: var(--chalk);
  }
  .menu-toggle span:nth-child(1) { top: 17px; }
  .menu-toggle span:nth-child(2) { top: 26px; }
  .menu-toggle span:nth-child(3) { top: 35px; }
  .site-title {
    position: absolute; left: 0; top: 0;
    width: 1200px; line-height: 55px;
    text-align: center;
    font-size: 30px; font-weight: 400;
    letter-spacing: 1px;
  }
  .brand-mark {
    position: absolute; left: 0; top: 150px;
    width: 1200px;
    text-align: center;
    font-size: 118px; font-weight: 400;
    letter-spacing: 6px;
    color: var(--logo-chalk);
  }
  .video-frame {
    position: absolute; left: 384px; top: 425px;
    width: 440px; height: 266px;
    background: var(--frame);
    padding: 8px;
  }
  .video-screen {
    position: relative; width: 100%; height: 100%;
    background: radial-gradient(ellipse at 45% 45%, var(--screen-1) 0%, var(--screen-2) 80%);
  }
  .video-screen svg { position: absolute; left: 0; top: 0; }
  .tagline {
    position: absolute; left: 0; top: 714px;
    width: 1200px;
    text-align: center;
    font-size: 35px; font-weight: 400;
    letter-spacing: 1px;
  }
  .enter-button {
    position: absolute; left: 479px; top: 776px;
    width: 250px; height: 45px;
    border-radius: 8px;
    background: var(--button-bg);
    color: var(--button-ink);
    text-align: center; line-height: 45px;
    font-size: 21px; font-weight: 700;
    text-decoration: none;
  }
  .copyright {
    position: absolute; left: 0; top: 843px;
    width: 1200px; text-align: center;
    font-family: Arial, Helvetica, sans-serif;
    font-size: 12.5px; color: var(--chalk);
  }
</style>
</head>
<body>
<main class="page">
  <header class="topbar">
    <div class="menu-toggle" aria-label="Menu"><span></span><span></span><span></span></div>
    <h1 class="site-title">QUILLMARK</h1>
  </header>

  <div class="brand-mark">QUILLMARK</div>

  <section class="video-frame">
    <div class="video-screen" role="img" aria-label="Video still: dark smoky backdrop with the product title in chalk lettering">
      <svg width="424" height="250" viewBox="0 0 424 250" aria-hidden="true">
        <circle cx="212" cy="113" r="46" fill="#ffffff" fill-opacity="0.72"/>
        <polygon points="199,93 199,133 232,113" fill="#111111"/>
        <rect x="0" y="226" width="424" height="24" fill="#0d0d0d"/>
        <rect x="0" y="224" width="424" height="3" fill="#444444"/>
        <rect x="0" y="224" width="22" height="3" fill="var(--accent-red)"/>
        <rect x="10" y="233" width="3" height="9" fill="#bbbbbb"/>
        <rect x="16" y="233" width="3" height="9" fill="#bbbbbb"/>
        <polygon points="31,236 35,236 39,232 39,244 35,240 31,240" fill="#bbbbbb"/>
        <rect x="50" y="236" width="24" height="4" fill="#777777"/>
        <circle cx="374" cy="238" r="4" fill="#999999"/>
        <rect x="386" y="234" width="10" height="8" fill="none" stroke="#999999" stroke-width="1.5"/>
        <rect x="403" y="233" width="12" height="10" fill="none" stroke="#999999" stroke-width="1.5" stroke-dasharray="4 4"/>
      </svg>
    </div>
  </section>

  <h2 class="tagline">A HIDDEN LEDGER OF SOCIAL OUTREACH CRAFTWORK</h2>

  <a class="enter-button" href="#">ENTER NOW</a>

  <footer class="copyright">Copyright © 2014 Quillmark</footer>
</main>
</body>
</html>
```